Biz Card for Harrowfield Property Partners - HWPP

Harrowfield Property Partners is a commercial real estate acquisitions firm. We buy commercial property and need to raise capital from investors for each deal we buy. The vibe needs to be: give us your money, we will multiply it.
Our website: www.hrwpp-example.com
Competitors are: https://velmarholdings-example.com/, https://tribanquepartners-example.com/, http://www.ostrellecapital-example.com/
Target Market(s)
High Net Worth Individuals, Bankers, Insurance Companies, Commercial Real Estate Brokers.
Industry/Entity Type
Investment Banking
Contact Information for Business Card
Name, Title, Addess, Cell#, Office#, email, website
Requirements
Must have
- use one of our logos. See website for look and feel: www.hrwpp-example.com
Nice to have
- see website: www.hrwpp-example.com

```html
<!DOCTYPE html>
<html lang="en">
<head>
<meta charset="utf-8">
<title>Harrowfield Property Partners — Business Card</title>
<link rel="stylesheet" href="https://fonts.googleapis.com/css2?family=Josefin+Sans:wght@300;400;600&display=swap">
<style>
  :root {
    --backdrop: #e9e9e9;
    --card-white: #f2f2f2;
    --navy: #0e2440;
    --navy-deep: #0a1f38;
    --ocean: #0a4f86;
    --text-grey: #7a7a7a;
    --rule-grey: #8d8d8d;
    --white: #ffffff;
  }
  * { margin: 0; padding: 0; box-sizing: border-box; }
  html, body {
    width: 1200px; height: 1200px; overflow: hidden;
    background: var(--backdrop);
    font-family: "Josefin Sans", sans-serif;
  }
  .card {
    position: absolute;
    left: 227px;
    width: 745px; height: 425px;
    border-radius: 38px;
    overflow: hidden;
  }
  .card--front { top: 135px; background: var(--card-white); }
  .card--back  { top: 640px; }

  .brand {
    position: absolute; top: 34px; right: 31px;
    display: flex; align-items: center; gap: 18px;
    color: var(--navy);
  }
  .brand__dot {
    width: 106px; height: 106px; border-radius: 50%;
    background: var(--navy);
  }
  .brand__name {
    font-weight: 400; color: var(--navy);
    text-transform: uppercase; line-height: 1;
  }
  .brand__name-main { display: block; font-size: 34px; letter-spacing: 0.16em; }
  .brand__name-sub  { display: block; font-size: 17px; letter-spacing: 0.28em; margin-top: 12px; }

  .person { position: absolute; left: 33px; top: 217px; }
  .person__name {
    font-size: 27px; font-weight: 600; color: var(--navy);
    letter-spacing: 0.01em; text-transform: uppercase;
  }
  .person__title {
    font-size: 18px; font-weight: 300; color: var(--text-grey);
    margin-top: 4px; letter-spacing: 0.03em;
  }

  .divider {
    position: absolute; left: 0; right: 0; top: 291px;
    height: 2px; background: var(--rule-grey);
  }
  .divider__accent {
    position: absolute; left: 33px; top: 0;
    width: 228px; height: 2px; background: var(--navy);
  }

  .contact { position: absolute; left: 33px; top: 318px; list-style: none; }
  .contact__item {
    display: flex; align-items: center; gap: 11px;
    font-size: 18px; font-weight: 300; color: var(--text-grey);
    height: 25.5px; letter-spacing: 0.02em;
  }
  .contact__icon { width: 18px; height: 18px; flex: none; }
  .contact__strong { font-weight: 600; color: var(--navy); }

  .address {
    position: absolute; right: 31px; top: 345px;
    text-align: right; font-size: 18px; font-weight: 300;
    color: var(--text-grey); line-height: 25px; letter-spacing: 0.03em;
  }

  .back-field {
    position: absolute; inset: 0;
    background: linear-gradient(105deg, var(--navy-deep) 0%, var(--navy-deep) 35%, var(--ocean) 85%);
  }
  .back-spot {
    position: absolute; left: 577px; top: 247px;
    width: 55px; height: 55px; border-radius: 50%;
    background: var(--white);
  }
</style>
</head>
<body>

<section class="card card--front" aria-label="Business card front">
  <div class="brand">
    <div class="brand__dot"></div>
    <div class="brand__name">
      <span class="brand__name-main">Harrowfield</span>
      <span class="brand__name-sub">Property Partners</span>
    </div>
  </div>

  <div class="person">
    <h1 class="person__name">Daniel R. Okonkwo</h1>
    <p class="person__title">Director of Finance</p>
  </div>

  <div class="divider"><div class="divider__accent"></div></div>

  <ul class="contact">
    <li class="contact__item">
      <svg class="contact__icon" viewBox="0 0 18 18" aria-hidden="true">
        <circle cx="9" cy="9" r="9" fill="var(--navy)"/>
        <path d="M4.5 8 Q9 4.5 13.5 8 L12.5 9.5 L11 8.7 L11 7.8 Q9 7 7 7.8 L7 8.7 L5.5 9.5 Z M6 10.5 H12 V13 H6 Z" fill="var(--white)"/>
      </svg>
      (555) 014-2290
    </li>
    <li class="contact__item">
      <svg class="contact__icon" viewBox="0 0 18 18" aria-hidden="true">
        <circle cx="9" cy="9" r="9" fill="var(--navy)"/>
        <rect x="4.5" y="6" width="9" height="6.5" fill="none" stroke="var(--white)" stroke-width="1.1"/>
        <path d="M4.5 6 L9 9.8 L13.5 6" fill="none" stroke="var(--white)" stroke-width="1.1"/>
      </svg>
      info@hrwpp-example.com
    </li>
    <li class="contact__item">
      <svg class="contact__icon" viewBox="0 0 18 18" aria-hidden="true">
        <circle cx="9" cy="9" r="9" fill="var(--navy)"/>
        <circle cx="9" cy="9" r="5" fill="none" stroke="var(--white)" stroke-width="1.1"/>
        <path d="M4 9 H14 M9 4 Q6 9 9 14 M9 4 Q12 9 9 14" fill="none" stroke="var(--white)" stroke-width="1"/>
      </svg>
      <span>www.<span class="contact__strong">hrwpp-example</span>.com</span>
    </li>
  </ul>

  <p class="address">480 Linden Row, Suite 900<br>Westbrook, ST 00000</p>
</section>

<section class="card card--back" aria-label="Business card back">
  <div class="back-field" role="img" aria-label="Repeating pattern of the company emblem, fading from deep navy on the left to ocean blue on the right"></div>
  <div class="back-spot"></div>
</section>

</body>
</html>
```